SNACKS packaging uplift

We need to revamp the current popcorn design to a new more elegant , more premium and cleaner design. The new design should have allow the consumer to immediatly relate the new pack to the old design, and not think its a totally new brand. feel free to update the logo, product shots, but we would like to maintain the WHITE identity somehow.

```html
<!DOCTYPE html>
<html lang="en">
<head>
<meta charset="utf-8">
<title>KERNO Popcorn – Packaging Range</title>
<link rel="stylesheet" href="https://fonts.googleapis.com/css2?family=Cinzel:wght@400;600;700&family=Cairo:wght@400;500&display=swap">
<style>
  :root {
    --page: #ffffff;
    --pack-white: #f7f7f5;
    --cheese-light: #fbe27a;
    --cheese-mid: #f3c842;
    --cheese-deep: #eab43a;
    --cheese-band: #f0b744;
    --cheese-ink: #6b5a44;
    --cheese-ink-dark: #4e3e2a;
    --tomato-light: #f39c7a;
    --tomato-mid: #e8633f;
    --tomato-deep: #d2452b;
    --tomato-band: #d9412e;
    --tomato-ink: #9a2a2c;
    --tomato-ink-dark: #7a1620;
    --band-text-cheese: #6d5327;
    --band-text-tomato: #fbe8df;
    --badge: #c9daf0;
    --badge-ink: #8a3a2c;
    --logo-fill: #ffffff;
  }
  * { box-sizing: border-box; margin: 0; padding: 0; }
  html, body { width: 1200px; height: 1200px; overflow: hidden; background: var(--page); }
  .canvas { position: relative; width: 1200px; height: 1200px; }

  .pack {
    position: absolute; top: 239px; width: 508px; height: 693px;
    background: var(--pack-white);
    overflow: hidden;
    box-shadow: 0 10px 18px rgba(0,0,0,0.08);
  }
  .pack--cheese { left: 43px; }
  .pack--tomato { left: 637px; }

  .crimp {
    position: absolute; left: 0; width: 100%; height: 26px;
    display: flex; align-items: center; justify-content: center;
    font-family: "Cinzel", serif; font-size: 10.5px; font-weight: 600;
    letter-spacing: 0.6px; white-space: nowrap;
  }
  .crimp--top { top: 0; }
  .crimp--bottom { bottom: 0; }
  .pack--cheese .crimp { background: var(--cheese-mid); color: var(--band-text-cheese); }
  .pack--tomato .crimp { background: var(--tomato-band); color: var(--band-text-tomato); }

  .upper {
    position: absolute; top: 26px; left: 0; width: 100%; height: 236px;
  }
  .pack--cheese .upper { background: linear-gradient(90deg, var(--cheese-mid), var(--cheese-light) 45%, var(--cheese-mid)); }
  .pack--tomato .upper { background: linear-gradient(90deg, var(--tomato-deep), var(--tomato-light) 45%, var(--tomato-mid)); }

  .brand {
    position: absolute; top: 46px; left: 0; width: 100%;
    display: flex; align-items: center; justify-content: center; gap: 14px;
  }
  .brand__name {
    font-family: "Cinzel", serif; font-weight: 700; font-size: 92px; line-height: 1;
    color: var(--logo-fill); letter-spacing: 2px;
  }
  .brand__dot { width: 12px; height: 12px; border-radius: 50%; background: var(--logo-fill); }

  .flavor-band {
    position: absolute; top: 258px; left: 0; width: 100%; height: 80px;
    display: flex; flex-direction: column; align-items: center; justify-content: center;
    clip-path: polygon(0 6px, 100% 6px, 100% calc(100% - 6px), 0 calc(100% - 6px));
  }
  .pack--cheese .flavor-band { background: var(--cheese-band); color: var(--cheese-ink); }
  .pack--tomato .flavor-band { background: var(--tomato-band); color: #fdeee8; }
  .flavor-band__en { font-family: "Cinzel", serif; font-size: 25px; font-weight: 400; letter-spacing: 0.5px; line-height: 1.1; }
  .flavor-band__ar { font-family: "Cairo", sans-serif; font-size: 20px; line-height: 1.2; direction: rtl; }

  .product-name {
    position: absolute; top: 345px; left: 0; width: 100%; text-align: center;
  }
  .product-name__en { font-family: "Cinzel", serif; font-size: 56px; font-weight: 400; line-height: 1; letter-spacing: 1px; }
  .product-name__ar { font-family: "Cairo", sans-serif; font-size: 28px; line-height: 1.3; direction: rtl; }
  .pack--cheese .product-name { color: var(--cheese-ink-dark); }
  .pack--tomato .product-name { color: var(--tomato-ink); }

  .badge {
    position: absolute; top: 405px; left: 395px; width: 100px; height: 96px;
    border-radius: 48% 52% 46% 54% / 50% 48% 52% 50%;
    background: var(--badge);
    display: flex; align-items: center; justify-content: center; text-align: center;
    font-family: "Cinzel", serif; font-size: 19px; line-height: 1.05; color: var(--badge-ink);
  }

  .product-shot {
    position: absolute; top: 450px; left: 70px; width: 340px; height: 200px;
    border-radius: 50% 50% 12px 12px / 40% 40% 12px 12px;
  }
  .pack--cheese .product-shot { background: radial-gradient(ellipse at 55% 45%, #f6c743, #f0b23a 55%, rgba(240,178,58,0.15) 90%); }
  .pack--tomato .product-shot { background: radial-gradient(ellipse at 55% 45%, #e2351f, #b8211a 50%, rgba(90,120,60,0.25) 90%); }
</style>
</head>
<body>
<main class="canvas">

  <section class="pack pack--cheese" aria-label="Nacho cheese flavour popcorn pack">
    <div class="crimp crimp--top">Nacho Cheese Flavor Popcorn · Nacho Cheese Flavor Popcorn</div>
    <div class="upper"></div>
    <div class="brand"><span class="brand__name">KERNO</span><span class="brand__dot"></span></div>
    <div class="flavor-band">
      <p class="flavor-band__en">Nacho Cheese Flavor</p>
      <p class="flavor-band__ar">نكهة جبنة الناتشو</p>
    </div>
    <div class="product-name">
      <h2 class="product-name__en">POPCORN</h2>
      <p class="product-name__ar">الفشار</p>
    </div>
    <div class="product-shot" role="img" aria-label="Wedge of yellow cheese with popcorn scattered around it"></div>
    <div class="badge">Air<br>Popped</div>
    <div class="crimp crimp--bottom">Nacho Cheese Flavor Popcorn · Nacho Cheese Flavor Popcorn</div>
  </section>

  <section class="pack pack--tomato" aria-label="Tomato and herb flavour popcorn pack">
    <div class="crimp crimp--top">Tomato &amp; Herb Flavor Popcorn · Tomato &amp; Herb Flavor Popcorn</div>
    <div class="upper"></div>
    <div class="brand"><span class="brand__name">KERNO</span><span class="brand__dot"></span></div>
    <div class="flavor-band">
      <p class="flavor-band__en">Tomato &amp; Herb Flavor</p>
      <p class="flavor-band__ar">نكهة جبنة الناتشو</p>
    </div>
    <div class="product-name">
      <h2 class="product-name__en">POPCORN</h2>
      <p class="product-name__ar">الفشار</p>
    </div>
    <div class="product-shot" role="img" aria-label="Fresh red tomato with rosemary and basil leaves and popcorn"></div>
    <div class="badge">Air<br>Popped</div>
    <div class="crimp crimp--bottom">Tomato &amp; Herb Flavor Popcorn · Tomato &amp; Herb Flavor Popcorn</div>
  </section>

</main>
</body>
</html>
```